Business Card for Bright Meadow Lawn & Landscape

Double Sided Card Design - I think one side of the card should be cleaner, with logo, contact info, and "Complete Residential & Commercial Landscape Services", and on the other side it should list the services we offer:

- Lawn Care & Mowing
- Hedge & Shrub Trimming
- Leaf Removal & Clean Up
- Aeration & Sod
- Mulch & Rock Installations
- Landscape Installations & Renovations
- Commercial Snow Removal

Please make it clean and very professional... don't want it too be too busy, but want to tell them what we do.

Target Market(s)

Residential and Commercial

Industry/Entity Type

Landscape

Contact Information for Business Card

Fully Insured
Tom Berrigan
410-555-0198
Tberrigan07@mailbox-example.com

Requirements
Must have
• Double Sided, Cleaner on one side, more information and text on the other side.

```html
<!DOCTYPE html>
<html lang="en">
<head>
<meta charset="UTF-8">
<title>Bright Meadow Lawn &amp; Landscape — Business Card</title>
<link href="https://fonts.googleapis.com/css2?family=Roboto:wght@300;400;500&display=swap" rel="stylesheet">
<style>
  :root {
    --page-bg: #2a2b2d;
    --card-white: #f6f7f5;
    --green-light: #8cc63f;
    --green-mid: #6aa832;
    --green-dark: #3f7a22;
    --charcoal: #2c3033;
    --charcoal-light: #3a3f43;
    --ink: #1e1f20;
    --text-light: #f4f8ee;
  }
  * { margin: 0; padding: 0; box-sizing: border-box; }
  html, body { width: 1200px; height: 959px; overflow: hidden; }
  body {
    background: var(--page-bg);
    font-family: "Roboto", Arial, sans-serif;
    position: relative;
  }
  .card {
    position: absolute;
    left: 250px;
    width: 700px;
    height: 400px;
    overflow: hidden;
    box-shadow: 0 14px 30px rgba(0,0,0,.45);
  }
  .card--services { top: 52px; background: var(--card-white); }
  .card--contact { top: 507px; }

  /* Services side */
  .services__band {
    position: absolute; left: 0; right: 0; bottom: 0; height: 140px;
    background: linear-gradient(180deg, var(--green-mid), var(--green-dark));
  }
  .services__content {
    position: absolute; left: 0; right: 0; top: 58px;
    text-align: center;
  }
  .services__title {
    font-weight: 400; font-size: 30px; letter-spacing: .5px;
    color: var(--green-light);
  }
  .services__rule {
    width: 480px; height: 2px; margin: 8px auto 18px;
    background: var(--green-light);
  }
  .services__list {
    list-style: none; color: var(--ink);
    font-size: 19px; line-height: 27px; font-weight: 400;
  }

  /* Contact side */
  .contact__panel {
    position: absolute; left: 0; top: 0; bottom: 0; width: 400px;
    background: radial-gradient(circle at 55% 35%, var(--green-light), var(--green-mid) 70%, var(--green-dark) 120%);
  }
  .contact__brandpanel {
    position: absolute; right: 0; top: 0; bottom: 0; width: 300px;
    background: linear-gradient(160deg, var(--charcoal), var(--charcoal-light));
  }
  .contact__details {
    position: absolute; left: 52px; top: 78px; color: var(--text-light);
  }
  .contact__name { font-size: 33px; font-weight: 300; letter-spacing: 1px; margin-bottom: 10px; }
  .contact__line { font-size: 18px; font-weight: 300; line-height: 28px; }
  .contact__tagline {
    position: absolute; left: 52px; bottom: 52px; color: var(--text-light);
    font-size: 19px; font-weight: 300; line-height: 24px;
  }
  .brand {
    position: absolute; left: 0; right: 0; top: 120px; text-align: center;
  }
  .brand__mark {
    width: 58px; height: 58px; border-radius: 50%;
    border: 5px solid var(--green-light); margin: 0 auto 14px;
  }
  .brand__name {
    color: var(--green-light); font-size: 20px; font-weight: 400;
    line-height: 26px; letter-spacing: 1px; text-transform: uppercase;
  }
  .contact__insured {
    position: absolute; left: 0; right: 0; bottom: 86px; text-align: center;
    color: var(--green-light); font-size: 20px; font-weight: 400; letter-spacing: .5px;
  }
</style>
</head>
<body>
  <section class="card card--services">
    <div class="services__band" role="img" aria-label="Green band with subtle grass texture"></div>
    <div class="services__content">
      <h2 class="services__title">SERVICES WE OFFER:</h2>
      <div class="services__rule"></div>
      <ul class="services__list">
        <li>• Lawn Care &amp; Mowing • Hedge &amp; Shrub Trimming</li>
        <li>• Leaf Removal &amp; Clean Up • Aeration &amp; Sod</li>
        <li>• Mulch &amp; Rock Installations</li>
        <li>• Landscape Installations &amp; Renovations</li>
        <li>• Commercial Snow Removal</li>
      </ul>
    </div>
  </section>

  <section class="card card--contact">
    <div class="contact__panel" role="img" aria-label="Green panel with subtle grass texture"></div>
    <div class="contact__details">
      <h1 class="contact__name">TOM BERRIGAN</h1>
      <p class="contact__line">P:410-555-0198</p>
      <p class="contact__line">E: Tberrigan07@mailbox-example.com</p>
    </div>
    <p class="contact__tagline">Complete<br>Residential &amp; Commercial<br>Landscape Services</p>
    <div class="contact__brandpanel">
      <div class="brand">
        <div class="brand__mark"></div>
        <p class="brand__name">Bright Meadow<br>Lawn &amp; Landscape</p>
      </div>
      <p class="contact__insured">FULLY INSURED</p>
    </div>
  </section>
</body>
</html>
```